Varlow's Electrical & Solar - Business Cards

I want my business card to stand out from the rest. I will provide my business name logo and my icon logo to be implemented onto the card.

On the front of the card, can i have the following. Just make it neat & professional please.

Dean Harrop
varlowselectrical@mailbox-example.net
0491 837 562
ABN: 41 269 507 813
License No. 582146K
FREE QUOTES
24/7 Emergency

On the back of the card, can I have "Our Services" and maybe add the V logo on the back in the background or something. Under "Our Services" I want the following:

LED Lighting Upgrades
Switches & Outlets
Smoke Alarms
Switchboard Upgrades
Fault Finding
Rewiring
New Builds
Test & Tagging
All Electrical Maintenance & Repairs

Can you guys add the instagram logo and next to it, put varlows_electrical

Can you guys also add the facebook logo and next to it put Varlow's Electrical & Solar. Make sure the instagram & facebook icon is in either white, green or black.

Also I have put down double sided, not sure why when i save it, it keeps going to single sided. I need my business card double sided.

New Customers

Dean Harrop varlowselectrical@mailbox-example.net 0491 837 562 ABN: 41 269 507 813 License No. 582146K FREE QUOTES 24/7 Emergency

• must be tidy, professional and appealing

```html
<!DOCTYPE html>
<html lang="en">
<head>
<meta charset="utf-8">
<title>Varlow's Electrical &amp; Solar – Business Cards</title>
<link rel="stylesheet" href="https://fonts.googleapis.com/css2?family=Arimo:wght@400;700&display=swap">
<style>
  :root {
    --bg: #e9e9ea;
    --card: #050505;
    --white: #f2f2f2;
    --green: #35c24a;
    --green-bright: #49d95e;
    --green-deep: #1f9a33;
    --grey: #9a9a9a;
    --divider: #3a3a3a;
  }
  * { box-sizing: border-box; margin: 0; padding: 0; }
  html, body { width: 1200px; height: 912px; overflow: hidden; }
  body {
    background: var(--bg);
    font-family: "Arimo", Arial, sans-serif;
    position: relative;
  }
  .card {
    position: absolute;
    left: 250px;
    width: 700px;
    height: 400px;
    background: var(--card);
    color: var(--white);
    overflow: hidden;
    box-shadow: 0 6px 18px rgba(0,0,0,.25);
  }
  .card--back { top: 36px; }
  .card--front { top: 476px; }

  /* back side */
  .brand-mark {
    position: absolute;
    right: 150px;
    top: 26px;
    width: 118px;
    height: 118px;
    border: 7px solid var(--green);
    border-radius: 50%;
  }
  .services {
    position: absolute;
    left: 52px;
    top: 150px;
    list-style: none;
  }
  .services li {
    font-size: 18px;
    line-height: 24.5px;
    position: relative;
    padding-left: 20px;
  }
  .services li::before {
    content: "";
    position: absolute;
    left: 2px;
    top: 9px;
    width: 7px;
    height: 7px;
    border-radius: 50%;
    background: var(--green);
  }
  .social {
    position: absolute;
    left: 430px;
    top: 250px;
    list-style: none;
  }
  .social li {
    display: flex;
    align-items: center;
    gap: 10px;
    font-size: 16px;
    line-height: 22px;
  }
  .social .dot {
    width: 14px;
    height: 14px;
    border-radius: 50%;
    background: var(--green);
    flex: none;
  }

  /* front side */
  .wordmark {
    position: absolute;
    left: 36px;
    top: 178px;
    width: 270px;
    font-size: 24px;
    font-weight: 700;
    line-height: 30px;
    color: var(--green);
  }
  .divider {
    position: absolute;
    left: 318px;
    top: 40px;
    width: 2px;
    height: 200px;
    background: var(--divider);
  }
  .contact {
    position: absolute;
    left: 345px;
    top: 42px;
  }
  .contact__name {
    font-size: 24px;
    font-weight: 400;
    letter-spacing: 1px;
    color: var(--green);
    margin-bottom: 8px;
    text-transform: uppercase;
  }
  .contact__line {
    font-size: 16px;
    line-height: 21px;
  }
  .contact__reach { margin-top: 14px; }
  .contact__reach .contact__line {
    display: flex;
    align-items: center;
    gap: 9px;
  }
  .contact__reach svg { width: 13px; height: 13px; flex: none; }
  .tagline {
    position: absolute;
    left: 0;
    right: 0;
    top: 286px;
    text-align: center;
    font-size: 19px;
    color: var(--white);
    padding-left: 120px;
  }
  .tagline .sep { color: var(--green); margin: 0 8px; }
  .band-line {
    position: absolute;
    left: 0; right: 0;
    bottom: 34px;
    height: 4px;
    background: var(--grey);
  }
  .band {
    position: absolute;
    left: 0; right: 0;
    bottom: 0;
    height: 30px;
    background: linear-gradient(90deg, var(--green-deep), var(--green-bright));
  }
</style>
</head>
<body>

<section class="card card--back" aria-label="Card back">
  <div class="brand-mark" aria-label="Varlow's Electrical &amp; Solar mark"></div>
  <ul class="services">
    <li>LED Lighting Upgrades</li>
    <li>Switches &amp; Outlets</li>
    <li>Smoke Alarms</li>
    <li>Switchboard Upgrades</li>
    <li>Fault Finding</li>
    <li>Rewiring</li>
    <li>New Builds</li>
    <li>Test &amp; Tagging</li>
    <li>All Electrical Maintenance &amp; Repairs</li>
  </ul>
  <ul class="social">
    <li><span class="dot"></span>Varlow's Electrical &amp; Solar</li>
    <li><span class="dot"></span>varlows_electrical</li>
  </ul>
</section>

<section class="card card--front" aria-label="Card front">
  <div class="wordmark">Varlow's Electrical &amp; Solar</div>
  <div class="divider"></div>
  <div class="contact">
    <h1 class="contact__name">Dean Harrop</h1>
    <p class="contact__line">ABN: 41 269 507 813</p>
    <p class="contact__line">License No. 582146K</p>
    <div class="contact__reach">
      <p class="contact__line">
        <svg viewBox="0 0 24 24" aria-hidden="true"><path fill="#35c24a" d="M6.6 10.8a15.1 15.1 0 0 0 6.6 6.6l2.2-2.2a1 1 0 0 1 1-.25 11.4 11.4 0 0 0 3.6.57 1 1 0 0 1 1 1V20a1 1 0 0 1-1 1A17 17 0 0 1 3 4a1 1 0 0 1 1-1h3.5a1 1 0 0 1 1 1c0 1.25.2 2.46.57 3.6a1 1 0 0 1-.25 1z"/></svg>
        0491 837 562
      </p>
      <p class="contact__line">
        <svg viewBox="0 0 24 24" aria-hidden="true"><path fill="#35c24a" d="M2 5h20v14H2z"/><path fill="none" stroke="#050505" stroke-width="2" d="M2 5l10 8 10-8"/></svg>
        varlowselectrical@mailbox-example.net
      </p>
    </div>
  </div>
  <p class="tagline">FREE QUOTES<span class="sep">•</span>24/7 Emergency</p>
  <div class="band-line"></div>
  <div class="band"></div>
</section>

</body>
</html>
```